Coffee Fundraising Label for a coffee bag

We would like an update to a label for our coffee fundraising bags. We currently fundraise to all types of groups, schools, sports teams, etc... These are the labels that go out on our coffee fundraising bags. All the details are included in the label Design document attached. They need to be simple to read but playful as they are for fundraisers.

Target Market(s)

Anyone who fundraises. Sports teams, schools, bands, non-profits and many more...

Requirements
Must have
• the brief tells you what the must haves are..
• Must have the larkspur roast drives logo. If you see the sticker file perhaps placing the logo in one of those colors might look good. If you look at the colors on the sticker file, these at the colors we using on our new web site... would like the background color of the label to stay black, unless you can convince us otherwise
Nice to have
• see the brief...
Should not have
• See the brief....

```html
<!DOCTYPE html>
<html lang="en">
<head>
<meta charset="utf-8">
<title>Larkspur Roast Drives – Coffee Bag Label</title>
<link rel="stylesheet" href="https://fonts.googleapis.com/css2?family=Oswald:wght@400;500&family=Caveat:wght@500&display=swap">
<style>
  :root {
    --page-bg: #ffffff;
    --label-black: #000000;
    --brand-orange: #f6a21e;
    --ink-white: #ffffff;
    --dash-grey: #d9d9d9;
    --art-grey: #2a2a2a;
  }
  * { box-sizing: border-box; margin: 0; padding: 0; }
  html, body {
    width: 1200px; height: 678px; overflow: hidden;
    background: var(--page-bg);
  }
  .canvas { position: relative; width: 1200px; height: 678px; }
  .label {
    position: absolute; left: 388px; top: 29px;
    width: 424px; height: 620px;
    background: var(--label-black);
    font-family: "Oswald", "Arial Narrow", sans-serif;
    color: var(--ink-white);
    text-align: center;
  }
  .brand-badge {
    position: absolute; left: 136px; top: 12px;
    width: 152px; height: 152px; border-radius: 50%;
    background: var(--brand-orange);
    display: flex; align-items: center; justify-content: center;
  }
  .brand-name {
    font-family: "Oswald", "Arial Narrow", sans-serif;
    font-weight: 500; font-size: 21px; line-height: 1.1;
    text-transform: uppercase; letter-spacing: 1px;
    color: var(--label-black);
    width: 120px;
  }
  .script {
    font-family: "Caveat", cursive;
    font-weight: 500;
    color: var(--brand-orange);
    position: absolute; left: 0; width: 100%;
    line-height: 1;
  }
  .product-title { top: 172px; font-size: 44px; letter-spacing: 1.5px; }
  .fill-in-frame {
    position: absolute; left: 21px; top: 224px;
    width: 382px; height: 154px;
    border: 2px dashed var(--dash-grey);
    padding: 3px;
  }
  .fill-in-area { width: 100%; height: 100%; background: var(--ink-white); }
  .origin-details {
    position: absolute; top: 386px; left: 0; width: 100%;
    font-size: 16px; line-height: 23px; letter-spacing: 0.6px;
    text-transform: uppercase; font-weight: 400;
  }
  .thank-you { top: 433px; font-size: 36px; letter-spacing: 0.8px; }
  .cup-illustration {
    position: absolute; left: 111px; top: 481px;
    width: 202px; height: 104px;
    background: radial-gradient(ellipse at center, #3a3a3a 0%, var(--art-grey) 55%, var(--label-black) 100%);
    border-radius: 8px;
  }
  .web-address {
    position: absolute; top: 590px; left: 0; width: 100%;
    font-size: 13px; font-weight: 500; letter-spacing: 1px;
    color: var(--brand-orange); text-transform: uppercase;
  }
</style>
</head>
<body>
<main class="canvas">
  <section class="label">
    <div class="brand-badge">
      <span class="brand-name">Larkspur Roast Drives</span>
    </div>
    <h1 class="script product-title">Fresh Roasted Coffee</h1>
    <div class="fill-in-frame"><div class="fill-in-area"></div></div>
    <p class="origin-details">Roasted in Alder Creek, BC<br>100% Arabica Coffee</p>
    <p class="script thank-you">Thank you for your support!</p>
    <div class="cup-illustration" role="img" aria-label="Line drawing of a coffee cup on a saucer"></div>
    <p class="web-address">www.larkspurroast.ca</p>
  </section>
</main>
</body>
</html>
```